Custom Beer Labelling Company Needs a Flyer

We need a flyer designed to promote Hopwrapz, a new company in Sydney that helps home brewers create their own small batch beer labels. Main purpose of the flyer is to increase awareness of the service we offer and drive traffic to the Hopwrapz shopify site - www.hopwrapz-example.com.au.
Our value proposition is about being easy (less than 5 minutes), affordable (full set of labels from only $12) with good quality (water resistant synthetic labels that remove cleanly).
The flyer should suit A4 printing and will preferably include screenshot of the "Create your Label" tool on the site, and/or examples of our label templates. It may also include other information from our site such eg from the "About Us" or About Our Labels" pages.

Target Market(s)

Home brewers, mostly males aged 20-50

Industry/Entity Type

It Company

Colors
ec1f27
fee3d4
f9ba93
f68d4e
f37122
f78f20
faa54b
fbc994
ffffff

Requirements
Must have
• Drive customers to www.hopwrapz-example.com as call to action
Nice to have
• screenshot(s) and examples of labels

```html
<!DOCTYPE html>
<html lang="en">
<head>
<meta charset="utf-8">
<title>Hopwrapz – Small Batch Beer Labels Flyer</title>
<link href="https://fonts.googleapis.com/css2?family=Montserrat:ital,wght@0,400;0,500;0,600;0,700;0,800;1,800&family=Roboto+Condensed:wght@400;700&display=swap" rel="stylesheet">
<style>
  :root {
    --red: #ec1f27;
    --label-red: #b2363f;
    --orange: #f37122;
    --orange-mid: #f78f20;
    --orange-light: #faa54b;
    --peach: #fbc994;
    --white: #ffffff;
    --ink: #1a1a1a;
    --brand-brown: #5a3a22;
    --ui-grey: #e9e8e4;
    --ui-line: #c9c7c2;
    --ui-text: #555555;
  }
  * { margin: 0; padding: 0; box-sizing: border-box; }
  html, body { width: 957px; height: 1200px; overflow: hidden; background: var(--white); }
  body { font-family: 'Montserrat', sans-serif; color: var(--ink); }
  .flyer { position: relative; width: 957px; height: 1200px; overflow: hidden;
    background: linear-gradient(#f4f4f4 0, var(--white) 260px); }

  .band { position: absolute; left: 0; top: 0; width: 957px; height: 1200px; }

  .brand { position: absolute; left: 42px; top: 44px; display: flex; align-items: center; gap: 12px; }
  .brand-mark { width: 44px; height: 44px; background: var(--orange-mid); }
  .brand-name { font-weight: 700; font-size: 40px; color: var(--brand-brown); letter-spacing: 0.5px; }

  .headline { position: absolute; left: 0; right: 0; top: 130px; text-align: center; }
  .headline-main { font-weight: 800; font-size: 53px; color: var(--orange-mid); letter-spacing: 1px; line-height: 1; }
  .headline-sub { margin-top: 10px; font-weight: 600; font-size: 36px; line-height: 1; letter-spacing: 0.5px; }

  .url-pill { position: absolute; left: 50%; top: 238px; transform: translateX(-50%);
    background: var(--red); color: var(--white); border-radius: 8px; padding: 8px 24px;
    font-weight: 600; font-size: 26px; white-space: nowrap; box-shadow: 0 3px 0 #b5161c; }

  .value-prop { position: absolute; left: 59px; top: 318px; font-size: 20px; line-height: 1.35; font-weight: 500; }
  .value-prop strong { font-weight: 700; font-size: 24px; }
  .value-prop .hl { color: var(--orange-mid); font-weight: 700; font-size: 27px; }

  /* Laptop with label tool */
  .laptop { position: absolute; left: 59px; top: 396px; width: 712px; height: 344px; }
  .laptop-lid { position: absolute; left: 0; top: 0; width: 533px; height: 317px;
    background: #1c1c1c; border-radius: 14px 14px 2px 2px; border: 2px solid #9a9a9a; }
  .laptop-base { position: absolute; left: 0; top: 315px; width: 712px; height: 22px;
    background: linear-gradient(#e8e8e8, #b9b9b9); border-radius: 2px 2px 14px 14px;
    box-shadow: 0 8px 12px rgba(0,0,0,0.25); }
  .screen { position: absolute; left: 14px; top: 16px; width: 503px; height: 286px;
    background: var(--white); overflow: hidden; }

  .tool-nav { height: 30px; display: flex; align-items: center; justify-content: space-between;
    padding: 0 12px; border-bottom: 1px solid #ddd; }
  .tool-brand { font-weight: 700; font-size: 14px; color: var(--brand-brown); display: flex; align-items: center; gap: 4px; }
  .tool-brand i { width: 10px; height: 10px; background: var(--orange-mid); display: inline-block; }
  .tool-links { font-size: 5.5px; letter-spacing: 0.8px; color: #777; word-spacing: 2px; }

  .tool-preview { position: absolute; left: 0; top: 31px; width: 258px; height: 255px;
    background: linear-gradient(90deg, #5e1a1f, #9a2c34 30%, #7a2027 70%, #4a1216); }
  .label-card { position: absolute; left: 30px; top: 24px; width: 198px; height: 200px;
    background: var(--white); padding: 6px; box-shadow: 0 2px 6px rgba(0,0,0,0.35); }
  .label-inner { border: 2px solid var(--label-red); height: 100%; text-align: center;
    font-family: 'Roboto Condensed', sans-serif; }
  .label-title { color: var(--label-red); font-weight: 700; font-size: 24px; line-height: 1; padding: 8px 0 6px; }
  .label-panel { margin: 0 6px; background: var(--label-red); color: var(--white); height: 82px; padding-top: 14px; }
  .label-style { font-weight: 700; font-size: 15px; }
  .label-tag { font-size: 6px; font-weight: 700; margin-top: 6px; letter-spacing: 0.5px; }
  .label-meta { display: flex; justify-content: space-between; padding: 0 8px; margin-top: 10px; font-size: 5px; }
  .label-notes { font-size: 5px; color: var(--label-red); padding: 8px 8px 0; line-height: 1.4; }

  .tool-form { position: absolute; left: 258px; top: 31px; width: 245px; height: 255px;
    background: var(--ui-grey); padding: 7px 10px 0 12px; font-family: 'Roboto Condensed', sans-serif; }
  .form-title { font-family: 'Montserrat', sans-serif; font-weight: 500; font-size: 12px; color: #444; }
  .form-sub { font-size: 6px; color: #777; margin-bottom: 4px; }
  .form-row { display: flex; gap: 8px; margin-top: 3px; }
  .field { flex: 1; }
  .field-label { font-size: 5.5px; font-weight: 700; color: #555; letter-spacing: 0.4px; }
  .field-box { background: var(--white); border: 1px solid var(--ui-line); height: 13px; font-size: 7px;
    color: var(--ui-text); padding: 2px 3px; margin-top: 1px; }
  .field-box.tall { height: 26px; line-height: 1.35; }
  .swatches { display: flex; gap: 2px; margin-top: 2px; }
  .swatches span { width: 13px; height: 11px; }
  .icons, .sizes { display: flex; margin-top: 2px; background: var(--white); border: 1px solid var(--ui-line); height: 13px; font-size: 6px; }
  .icons span, .sizes span { flex: 1; text-align: center; line-height: 11px; color: #444; }
  .form-total { display: flex; align-items: center; justify-content: center; gap: 50px; margin-top: 9px; }
  .price { font-family: 'Montserrat', sans-serif; font-size: 11px; color: #555; }
  .add-btn { background: var(--red); color: var(--white); font-size: 7px; padding: 4px 8px; }

  .visual-bottles { position: absolute; left: 626px; top: 333px; width: 250px; height: 402px;
    border-radius: 30px 30px 14px 14px;
    background: linear-gradient(180deg, rgba(60,30,18,0) 0, #3a2214 18%, #3a2214 55%, #a3323f 56%, #b2363f 78%, #3a2214 79%, #2b1a10 100%); }

  .tagline { position: absolute; left: 50px; top: 772px; color: var(--white); font-weight: 700;
    font-size: 25px; line-height: 1.3; letter-spacing: 0.5px; }
  .tagline span { display: block; }
  .tagline .big { font-size: 27px; }

  .about { position: absolute; left: 42px; top: 910px; width: 382px; font-size: 14.5px; line-height: 1.33;
    text-align: justify; font-weight: 500; }

  .photo { position: absolute; top: 912px; width: 227px; height: 146px; }
  .photo-assorted { left: 448px; background: linear-gradient(180deg, #dedede, #8a6a4a 60%, #3b2616); }
  .photo-batch { left: 698px; background: linear-gradient(180deg, #5a5560, #3a1f16 50%, #7a2a30); }

  .cta { position: absolute; left: 0; right: 0; top: 1104px; text-align: center; }
  .cta-line { font-weight: 800; font-style: italic; font-size: 19px; letter-spacing: 0.3px; }
  .cta-url { margin-top: 8px; font-weight: 700; font-size: 22px; color: var(--orange-mid); }
</style>
</head>
<body>
<main class="flyer">
  <svg class="band" viewBox="0 0 957 1200" aria-hidden="true">
    <defs>
      <linearGradient id="bandFill" x1="0" y1="0" x2="0" y2="1">
        <stop offset="0" stop-color="#faa54b"/>
        <stop offset="0.5" stop-color="#f78f20"/>
        <stop offset="1" stop-color="#f37122"/>
      </linearGradient>
    </defs>
    <polygon points="0,503 957,405 957,786 0,890" fill="url(#bandFill)"/>
  </svg>

  <header class="brand">
    <span class="brand-mark"></span>
    <span class="brand-name">Hopwrapz</span>
  </header>

  <section class="headline">
    <h1 class="headline-main">EASY &amp; AFFORDABLE</h1>
    <p class="headline-sub">SMALL BATCH BEER LABELS AT</p>
  </section>

  <a class="url-pill">www.hopwrapz-example.com.au</a>

  <p class="value-prop">Less than <span class="hl">5 MINUTES</span> and from just <span class="hl">$12</span><br>for a <strong>full set of custom printed labels.</strong></p>

  <div class="laptop">
    <div class="laptop-lid">
      <div class="screen">
        <nav class="tool-nav">
          <span class="tool-brand"><i></i>Hopwrapz</span>
          <span class="tool-links">CREATE YOUR LABEL | ABOUT US | ABOUT OUR LABELS | BLOG</span>
        </nav>
        <div class="tool-preview">
          <div class="label-card">
            <div class="label-inner">
              <div class="label-title">Your Beer</div>
              <div class="label-panel">
                <div class="label-style">Beer Style</div>
                <div class="label-tag">YOUR TAGLINE</div>
                <div class="label-meta"><span>BREWED 04/05/16</span><span>ABV 0.0%</span><span>14/05/16 BOTTLED</span></div>
              </div>
              <div class="label-notes">Original Gravity: 1.010 · Final Gravity: 1.010</div>
            </div>
          </div>
        </div>
        <div class="tool-form">
          <div class="form-title">CREATE YOUR LABEL</div>
          <div class="form-sub">easy and affordable small batch beer labels</div>
          <div class="form-row">
            <div class="field"><div class="field-label">BEER NAME</div><div class="field-box">Your Beer</div></div>
            <div class="field"><div class="field-label">STYLE</div><div class="field-box">Beer Style</div></div>
          </div>
          <div class="form-row">
            <div class="field"><div class="field-label">BREWED BY</div><div class="field-box">Your Brewery</div></div>
            <div class="field"><div class="field-label">TAGLINE</div><div class="field-box">Your Tagline</div></div>
          </div>
          <div class="form-row">
            <div class="field"><div class="field-label">BREWED</div><div class="field-box">04/05/16</div></div>
            <div class="field"><div class="field-label">BOTTLED</div><div class="field-box">14/05/16</div></div>
            <div class="field"><div class="field-label">ABV</div><div class="field-box">0.0%</div></div>
          </div>
          <div class="form-row">
            <div class="field"><div class="field-label">ORIGINAL GRAVITY</div><div class="field-box">1010</div></div>
            <div class="field"><div class="field-label">FINAL GRAVITY</div><div class="field-box">1010</div></div>
          </div>
          <div class="form-row">
            <div class="field"><div class="field-label">NOTES</div><div class="field-box tall">This may include further brewing details such as grain bill, mash and sparge temperatures, boil time and hop additions</div></div>
          </div>
          <div class="form-row">
            <div class="field"><div class="field-label">COLOR</div>
              <div class="swatches"><span style="background:#111"></span><span style="background:#c8bd96"></span><span style="background:#4aa6a3"></span><span style="background:#b2363f"></span></div>
            </div>
            <div class="field"><div class="field-label">ICON</div>
              <div class="icons"><span>⚓</span><span>▲</span><span>✶</span></div>
            </div>
            <div class="field"><div class="field-label">BOTTLE TYPE</div>
              <div class="sizes"><span>Large</span><span>Small</span></div>
            </div>
          </div>
          <div class="form-total"><span class="price">$0.79</span><span class="add-btn">ADD</span></div>
        </div>
      </div>
    </div>
    <div class="laptop-base"></div>
  </div>

  <div class="visual-bottles" role="img" aria-label="Three brown beer bottles wearing red custom labels"></div>

  <h2 class="tagline"><span>TAKE YOUR HOMEBREW</span><span class="big">TO ANOTHER LEVEL</span></h2>

  <p class="about">Just fill in template with details of your brew, and select from our range of designs, colours, icons and bottle size. We print your labels in high quality LED on A4 sheets of die cut, self-adhesive labels. Our synthetic labels are water resistant and remove cleanly from your empties without tearing and without leftover glue crud.</p>

  <div class="photo photo-assorted" role="img" aria-label="Assorted homebrew bottles with different custom labels"></div>
  <div class="photo photo-batch" role="img" aria-label="A full batch of bottles with matching red labels"></div>

  <footer class="cta">
    <p class="cta-line">TRY A SET OF HOPWRAPZ NEXT TIME YOU PUT DOWN A BATCH.</p>
    <p class="cta-url">www.hopwrapz-example.com.au</p>
  </footer>
</main>
</body>
</html>
```